(LUMO VALE CONSULTANT SERVICE) Credit Repair Service

We are committed to customer service, Credit Repair Service, Consumer Finance, Landlord Tenant, Traffic, Estate Planning, Collection, Family Law, Civil Litigation, and so much more.

Kestrel Brook Prime Payment plans starting at $200 per month

Consumer Finance, Landlord Tenant, Traffic, Estate Planning, Collection, Family Law, Civil Litigation, and so much more

Credit Services

Tiered Corvanta $1,700

One-on-One consultations with a Certified ZORV© Professional

Bureau Challenges

Creditor Interventions

Inquiry Assist

Score Analysis

Report Watch

QuelNorth® Alerts

Cease & Desist Letters

ZORV® Score Tracker

Identity Protection

Personal Finance Tools

Premier Gold $1,400

Bureau Challenges

Creditor Interventions

Inquiry Assist

Score Analysis

Report Watch

QuelNorth® Alerts

Premier Bronze $,1150

Bureau Challenges

Creditor Interventions

Industry/Entity Type

Consulting

Coding

Coded - Design and coding required

Number of Pages Required

1 page

Colors
cee9f5
85cae6
ecf7fb

Requirements
Must have
• We are committed to customer service, Credit Repair Service, Consumer Finance, Landlord Tenant, Traffic, Estate Planning, Collection, Family Law, Civil Litigation, and so much more.
• Kestrel Brook Prime Payment plans starting at $200 per month
• Consumer Finance, Landlord Tenant, Traffic, Estate Planning, Collection, Family Law, Civil Litigation, and so much more
• Credit Services
• Tiered Corvanta $1,700
• One-on-One consultations with a Certified ZORV© Professional
• Bureau Challenges
• Creditor Interventions
• Inquiry Assist
• Score Analysis
• Report Watch
• QuelNorth® Alerts
• Cease & Desist Letters
• ZORV® Score Tracker
• Identity Protection
• Personal Finance Tools
• Premier Gold $1,400
• Bureau Challenges
• Creditor Interventions
• Inquiry Assist
• Score Analysis
• Report Watch
• QuelNorth® Alerts
• Premier Bronze $,1150
• Bureau Challenges
• Creditor Interventions
• Pricing, services, about us, generic pictures, contact information,
• Contact information -( mavis27dun@inboxmail.test) 4127 NW 218 Street Miami FL 33174
Nice to have

```html
<!DOCTYPE html>
<html lang="en">
<head>
<meta charset="utf-8">
<title>Lumo Vale Consultant Service – Credit Repair</title>
<link rel="stylesheet" href="https://fonts.googleapis.com/css2?family=Roboto:wght@400;500;700&family=Vollkorn:wght@500;600;700&display=swap">
<style>
:root{
  --sky:#cee9f5;
  --sky-mid:#85cae6;
  --sky-deep:#6fbbe0;
  --mist:#ecf7fb;
  --accent:#3a95c9;
  --tick:#4fa9d6;
  --ink:#1d1d1d;
  --text:#3a3a3a;
  --muted:#555;
  --white:#fff;
}
*{box-sizing:border-box;margin:0;padding:0}
html,body{width:1200px;height:2507px;overflow:hidden}
body{position:relative;background:var(--white);font-family:'Roboto',Arial,sans-serif;color:var(--text)}
.serif{font-family:'Vollkorn',Georgia,serif}
svg.defs{position:absolute;width:0;height:0}

/* header */
.topbar{position:absolute;left:0;top:0;width:1200px;height:37px;background:var(--sky)}
.brand-panel{position:absolute;left:0;top:0;width:242px;height:100px;background:var(--mist);clip-path:polygon(0 0,100% 0,86% 100%,0 100%)}
.brand{position:absolute;left:58px;top:18px;font-family:'Vollkorn',Georgia,serif;font-weight:700;font-size:38px;color:var(--accent);line-height:1}
.contact-strip{position:absolute;right:60px;top:0;height:37px;display:flex;gap:34px;align-items:center;font-size:14px;color:#333}
.contact-strip span{display:flex;align-items:center;gap:10px}
.nav{position:absolute;right:60px;top:60px;display:flex;gap:32px;font-size:14px;font-weight:500;color:#222;text-transform:uppercase}
.nav .active{color:var(--accent)}

/* hero */
.hero{position:absolute;left:0;top:100px;width:1200px;height:518px;background:linear-gradient(120deg,#3b3f46 0%,#8f9297 25%,#d8dadd 50%,#eeefef 70%,#b9b4ac 100%)}
.hero-curve{position:absolute;left:0;top:0}
.hero-title{position:absolute;left:50%;top:220px;transform:translateX(-50%);background:rgba(20,20,20,.72);color:#fff;font-family:'Vollkorn',Georgia,serif;font-weight:600;font-size:33px;padding:4px 24px;white-space:nowrap}
.hero-sub{position:absolute;left:50%;top:280px;transform:translateX(-50%);background:rgba(20,20,20,.72);color:#fff;font-size:22px;padding:4px 26px;white-space:nowrap}
.hero-down{position:absolute;left:576px;top:428px;width:46px;height:46px;border:2px solid rgba(255,255,255,.85);border-radius:50%;display:flex;align-items:center;justify-content:center}

/* welcome */
.welcome{position:absolute;left:90px;top:650px;width:1020px;text-align:center}
.section-title{font-family:'Vollkorn',Georgia,serif;font-weight:600;font-size:32px;color:var(--ink)}
.welcome p{margin-top:14px;font-size:15px;line-height:24px;color:var(--text)}
.btn{display:inline-flex;align-items:center;justify-content:center;background:var(--sky);color:#222;font-size:15px;font-weight:500}
.btn-read{position:absolute;left:535px;top:770px;width:130px;height:35px}

/* pricing */
.pricing{position:absolute;left:75px;top:839px;width:1050px;display:grid;grid-template-columns:262px 261px 260px 258px;grid-template-rows:97px repeat(11,45px);column-gap:3px;row-gap:1px;background:var(--white)}
.cell{display:flex;align-items:center;justify-content:center}
.cell.label{justify-content:flex-start;padding-left:22px;background:var(--mist);font-size:13.5px;line-height:22px;color:#222}
.cell.head-label{background:var(--sky);justify-content:flex-start;padding-left:24px;font-family:'Vollkorn',Georgia,serif;font-weight:700;font-size:24px;color:var(--ink)}
.cell.top{background:var(--sky-deep)}
.cell.std{background:var(--sky)}
.plan{flex-direction:column;gap:2px;text-align:center}
.plan-name{font-family:'Vollkorn',Georgia,serif;font-size:18px;text-transform:uppercase;letter-spacing:.5px;color:#222}
.plan-price{font-size:33px;font-weight:700;color:#111}
.top .plan-name,.top .plan-price{color:#fff}
.mark{width:20px;height:20px}

/* services */
.services-title{position:absolute;left:0;width:1200px;top:1484px;text-align:center}
.service{position:absolute;width:360px}
.service svg.icon{position:absolute;left:0;top:0;width:56px;height:56px}
.service h3{margin-left:74px;font-family:'Vollkorn',Georgia,serif;font-weight:600;font-size:18px;color:var(--accent)}
.service p{margin-left:74px;margin-top:8px;width:270px;font-size:14px;line-height:24px;text-align:justify;color:var(--text)}
.btn-more{position:absolute;left:490px;top:2050px;width:220px;height:40px;font-size:16px}

/* footer */
.footer{position:absolute;left:0;top:2139px;width:1200px;height:309px;background:var(--mist)}
.footer-brand{position:absolute;left:62px;top:58px;font-family:'Vollkorn',Georgia,serif;font-weight:700;font-size:38px;color:var(--ink);line-height:1}
.footer-contact{position:absolute;left:62px;top:127px;font-size:14px;line-height:27px;color:#222}
.footer-contact div{display:flex;gap:14px}
.footer-contact svg{flex:none;margin-top:7px}
.footer-col{position:absolute;top:58px}
.footer-col h4{font-size:18px;font-weight:500;color:#222;margin-bottom:14px}
.footer-col ul{list-style:none;font-size:14px;color:#222}
.footer-col li{height:27.5px;display:flex;align-items:center;gap:22px}
.footer-col .sq{width:9px;height:9px;background:#222}
.form{position:absolute;left:774px;top:92px;width:366px}
.field{position:absolute;background:var(--white);font-size:12px;color:#777;padding:8px 10px}
.submit{position:absolute;left:0;top:142px;width:92px;height:37px;font-size:16px}
.copyright{position:absolute;left:60px;top:2466px;font-size:12px;color:#222}
</style>
</head>
<body>

<svg class="defs" aria-hidden="true">
  <symbol id="tick" viewBox="0 0 20 20"><path d="M3 10.5l4.5 4.5L17 5" fill="none" stroke="currentColor" stroke-width="3" stroke-linecap="round" stroke-linejoin="round"/></symbol>
  <symbol id="cross" viewBox="0 0 20 20"><path d="M5 5l10 10M15 5L5 15" fill="none" stroke="currentColor" stroke-width="3.2" stroke-linecap="round"/></symbol>
  <symbol id="pin" viewBox="0 0 12 16"><path d="M6 0a6 6 0 0 0-6 6c0 4.5 6 10 6 10s6-5.5 6-10a6 6 0 0 0-6-6zm0 8.5A2.5 2.5 0 1 1 6 3.5a2.5 2.5 0 0 1 0 5z" fill="currentColor"/></symbol>
  <symbol id="mail" viewBox="0 0 16 12"><rect x="1" y="1" width="14" height="10" fill="none" stroke="currentColor" stroke-width="1.6"/><path d="M1 1l7 6 7-6" fill="none" stroke="currentColor" stroke-width="1.6"/></symbol>
  <symbol id="chev" viewBox="0 0 10 14"><path d="M2 1l6 6-6 6" fill="none" stroke="currentColor" stroke-width="2.2"/></symbol>
</svg>

<!-- header -->
<div class="topbar"></div>
<div class="brand-panel"></div>
<div class="brand">Lumo Vale</div>
<div class="contact-strip">
  <span><svg width="16" height="12"><use href="#mail"/></svg>mavis27dun@inboxmail.test</span>
  <span><svg width="12" height="16"><use href="#pin"/></svg>4127 NW 218 Street Miami FL 33174</span>
</div>
<nav class="nav"><span class="active">Home</span><span>Pricing</span><span>Services</span><span>About us</span><span>Contact us</span></nav>

<!-- hero -->
<section class="hero" role="img" aria-label="Photo of a consultant reviewing credit documents with a couple at an office desk">
  <svg class="hero-curve" width="1200" height="518" aria-hidden="true"><path d="M0 430 Q600 606 1200 430 L1200 518 L0 518Z" fill="#fff"/></svg>
  <div class="hero-title" style="top:220px">We provide credit repair service</div>
  <div class="hero-sub" style="top:280px">Kestrel Brook Prime Payment plans starting at $200 per month</div>
  <div class="hero-down"><svg width="18" height="12"><path d="M2 2l7 7 7-7" fill="none" stroke="#fff" stroke-width="2"/></svg></div>
</section>

<!-- welcome -->
<section class="welcome">
  <h1 class="section-title">Welcome to Lumo Vale Consulting</h1>
  <p>Vitae ipsum arcu. Et praesent amet ac pulvinar diam. Vulputate sed neque. Scelerisque sem orci feugiat amet eu. Id dictumst libero nunc lorem lacus. Dolor dolor mollis. Nibh urna ornare. Curabitur culpa pharetra et et elit. Id semper facilisis.</p>
</section>
<a class="btn btn-read">Read more</a>

<!-- pricing -->
<section class="pricing">
  <div class="cell head-label">Credit Services</div>
  <div class="cell top plan"><span class="plan-name">Tiered Corvanta</span><span class="plan-price">$1,700</span></div>
  <div class="cell std plan"><span class="plan-name">Premier Gold</span><span class="plan-price">$1,400</span></div>
  <div class="cell std plan"><span class="plan-name">Premier Bronze</span><span class="plan-price">$,1150</span></div>

  <div class="cell label">One-on-One consultations with<br>a Certified ZORV© Professional</div>
  <div class="cell top"><svg class="mark" style="color:#fff"><use href="#tick"/></svg></div>
  <div class="cell std"><svg class="mark" style="color:var(--tick)"><use href="#tick"/></svg></div>
  <div class="cell std"><svg class="mark" style="color:#666;width:16px"><use href="#cross"/></svg></div>

  <div class="cell label">Bureau Challenges</div>
  <div class="cell top"><svg class="mark" style="color:#fff"><use href="#tick"/></svg></div>
  <div class="cell std"><svg class="mark" style="color:var(--tick)"><use href="#tick"/></svg></div>
  <div class="cell std"><svg class="mark" style="color:var(--tick)"><use href="#tick"/></svg></div>

  <div class="cell label">Creditor Interventions</div>
  <div class="cell top"><svg class="mark" style="color:#fff"><use href="#tick"/></svg></div>
  <div class="cell std"><svg class="mark" style="color:var(--tick)"><use href="#tick"/></svg></div>
  <div class="cell std"><svg class="mark" style="color:var(--tick)"><use href="#tick"/></svg></div>

  <div class="cell label">Inquiry Assist</div>
  <div class="cell top"><svg class="mark" style="color:#fff"><use href="#tick"/></svg></div>
  <div class="cell std"><svg class="mark" style="color:var(--tick)"><use href="#tick"/></svg></div>
  <div class="cell std"><svg class="mark" style="color:#666;width:16px"><use href="#cross"/></svg></div>

  <div class="cell label">Score Analysis</div>
  <div class="cell top"><svg class="mark" style="color:#fff"><use href="#tick"/></svg></div>
  <div class="cell std"><svg class="mark" style="color:var(--tick)"><use href="#tick"/></svg></div>
  <div class="cell std"><svg class="mark" style="color:#666;width:16px"><use href="#cross"/></svg></div>

  <div class="cell label">Report Watch</div>
  <div class="cell top"><svg class="mark" style="color:#fff"><use href="#tick"/></svg></div>
  <div class="cell std"><svg class="mark" style="color:var(--tick)"><use href="#tick"/></svg></div>
  <div class="cell std"><svg class="mark" style="color:#666;width:16px"><use href="#cross"/></svg></div>

  <div class="cell label">QuelNorth® Alerts</div>
  <div class="cell top"><svg class="mark" style="color:#fff"><use href="#tick"/></svg></div>
  <div class="cell std"><svg class="mark" style="color:var(--tick)"><use href="#tick"/></svg></div>
  <div class="cell std"><svg class="mark" style="color:#666;width:16px"><use href="#cross"/></svg></div>

  <div class="cell label">Cease &amp; Desist Letters</div>
  <div class="cell top"><svg class="mark" style="color:#fff"><use href="#tick"/></svg></div>
  <div class="cell std"><svg class="mark" style="color:#666;width:16px"><use href="#cross"/></svg></div>
  <div class="cell std"><svg class="mark" style="color:#666;width:16px"><use href="#cross"/></svg></div>

  <div class="cell label">ZORV® Score Tracker</div>
  <div class="cell top"><svg class="mark" style="color:#fff"><use href="#tick"/></svg></div>
  <div class="cell std"><svg class="mark" style="color:#666;width:16px"><use href="#cross"/></svg></div>
  <div class="cell std"><svg class="mark" style="color:#666;width:16px"><use href="#cross"/></svg></div>

  <div class="cell label">Identity Protection</div>
  <div class="cell top"><svg class="mark" style="color:#fff"><use href="#tick"/></svg></div>
  <div class="cell std"><svg class="mark" style="color:#666;width:16px"><use href="#cross"/></svg></div>
  <div class="cell std"><svg class="mark" style="color:#666;width:16px"><use href="#cross"/></svg></div>

  <div class="cell label">Personal Finance Tools</div>
  <div class="cell top"><svg class="mark" style="color:#fff"><use href="#tick"/></svg></div>
  <div class="cell std"><svg class="mark" style="color:#666;width:16px"><use href="#cross"/></svg></div>
  <div class="cell std"><svg class="mark" style="color:#666;width:16px"><use href="#cross"/></svg></div>
</section>

<!-- services -->
<h2 class="section-title services-title">What we do</h2>

<article class="service" style="left:62px;top:1562px">
  <svg class="icon" viewBox="0 0 56 56" fill="none" stroke="#222" stroke-width="2"><circle cx="28" cy="20" r="10"/><path d="M16 20a12 12 0 0 1 24 0M10 52c2-10 9-15 18-15s16 5 18 15z"/><rect x="13" y="18" width="4" height="8"/><rect x="39" y="18" width="4" height="8"/></svg>
  <h3>Customer service</h3>
  <p>Fusce nullam id. Velit proin magna vestibulum metus adipiscing. Integer urna incididunt lorem montes in varius adipiscing sem. Metus nibh.</p>
</article>
<article class="service" style="left:434px;top:1562px">
  <svg class="icon" viewBox="0 0 56 56" fill="none" stroke="#222" stroke-width="2"><path d="M8 48l24-24M30 18a9 9 0 0 1 12-10l-5 6 3 4 6-4a9 9 0 0 1-11 12"/><path d="M12 10l10 10M8 14l6-6 4 4-6 6zM32 34l14 14-4 4-14-14"/></svg>
  <h3>Credit Repair Service</h3>
  <p>Praesent vehicula wisi aenean vel mauris risus lacus non vestibulum fringilla at. Praesent vitae venenatis metus dolor ad. Lectus aenean pede.</p>
</article>
<article class="service" style="left:802px;top:1562px">
  <svg class="icon" viewBox="0 0 56 56" fill="none" stroke="#222" stroke-width="2"><circle cx="28" cy="12" r="8"/><path d="M28 20v10M10 30h36M10 30v8M28 30v8M46 30v8"/><circle cx="10" cy="43" r="5"/><circle cx="28" cy="43" r="5"/><circle cx="46" cy="43" r="5"/></svg>
  <h3>Consumer Finance</h3>
  <p>Vulputate sed neque. Scelerisque sem orci feugiat amet eu. Id dictumst libero nunc lorem lacus. Dolor dolor mollis. Nibh urna ornare. Curabitur culpa.</p>
</article>

<article class="service" style="left:62px;top:1720px">
  <svg class="icon" viewBox="0 0 56 56" fill="none" stroke="#222" stroke-width="2"><circle cx="14" cy="10" r="5"/><path d="M8 20h12v16h-3v14h-6V36H8zM26 28l14-12 14 12M30 25v25h20V25"/></svg>
  <h3>Landlord Tenant</h3>
  <p>Vulputate sed neque. Scelerisque sem orci feugiat amet eu. Id dictumst libero nunc lorem lacus. Dolor dolor mollis. Nibh urna ornare. Curabitur culpa.</p>
</article>
<article class="service" style="left:434px;top:1720px">
  <svg class="icon" viewBox="0 0 56 56" fill="none" stroke="#222" stroke-width="2.4"><path d="M12 24a17 17 0 0 1 28-10M44 32a17 17 0 0 1-28 10"/><path d="M40 6v9h-9M16 50v-9h9"/></svg>
  <h3>Traffic</h3>
  <p>Fusce nullam id. Velit proin magna vestibulum metus adipiscing. Integer urna incididunt lorem montes in varius adipiscing sem. Metus nibh.</p>
</article>
<article class="service" style="left:802px;top:1720px">
  <svg class="icon" viewBox="0 0 56 56" fill="none" stroke="#222" stroke-width="2"><rect x="10" y="4" width="14" height="48"/><path d="M10 12h6M10 20h8M10 28h6M10 36h8M10 44h6M34 8h10v36l-5 8-5-8zM34 14h10"/></svg>
  <h3>Estate Planning</h3>
  <p>Praesent vehicula wisi aenean vel mauris risus lacus non vestibulum fringilla at. Praesent vitae venenatis metus dolor ad. Lectus aenean pede.</p>
</article>

<article class="service" style="left:62px;top:1890px">
  <svg class="icon" viewBox="0 0 56 56" fill="none" stroke="#222" stroke-width="2"><rect x="18" y="6" width="32" height="20" transform="rotate(-12 34 16)"/><rect x="20" y="14" width="30" height="36"/><circle cx="35" cy="30" r="6"/><path d="M4 30h10v20H4zM14 34h8"/></svg>
  <h3>Collection</h3>
  <p>Fusce nullam id. Velit proin magna vestibulum metus adipiscing. Integer urna incididunt lorem montes in varius adipiscing sem. Metus nibh.</p>
</article>
<article class="service" style="left:434px;top:1890px">
  <svg class="icon" viewBox="0 0 56 56" fill="none" stroke="#222" stroke-width="2"><circle cx="17" cy="20" r="8"/><circle cx="39" cy="20" r="8"/><path d="M4 50c0-10 6-16 13-16s13 6 13 16M26 50c0-10 6-16 13-16s13 6 13 16"/></svg>
  <h3>Family Law</h3>
  <p>Praesent vehicula wisi aenean vel mauris risus lacus non vestibulum fringilla at. Praesent vitae venenatis metus dolor ad. Lectus aenean pede.</p>
</article>
<article class="service" style="left:802px;top:1890px">
  <svg class="icon" viewBox="0 0 56 56" fill="none" stroke="#222" stroke-width="2"><path d="M6 24h18v8H6zM15 32v14M6 48h18M30 20l10-9 10 9M33 18v12h14V18M26 28h26"/></svg>
  <h3>Civil Litigation</h3>
  <p>Vulputate sed neque. Scelerisque sem orci feugiat amet eu. Id dictumst libero nunc lorem lacus. Dolor dolor mollis. Nibh urna ornare. Curabitur culpa.</p>
</article>

<a class="btn btn-more">View More Details</a>

<!-- footer -->
<footer class="footer">
  <div class="footer-brand">Lumo Vale</div>
  <div class="footer-contact">
    <div><svg width="12" height="16"><use href="#pin"/></svg><span>4127 NW 218 Street Miami<br>FL 33174</span></div>
    <div style="margin-top:10px"><svg width="16" height="12"><use href="#mail"/></svg><span>mavis27dun@inboxmail.test</span></div>
  </div>

  <div class="footer-col" style="left:369px">
    <h4>Quick Links</h4>
    <ul>
      <li><svg width="10" height="14"><use href="#chev"/></svg>Home</li>
      <li><svg width="10" height="14"><use href="#chev"/></svg>Pricing</li>
      <li><svg width="10" height="14"><use href="#chev"/></svg>Services</li>
      <li><svg width="10" height="14"><use href="#chev"/></svg>About us</li>
      <li><svg width="10" height="14"><use href="#chev"/></svg>Contact us</li>
    </ul>
  </div>

  <div class="footer-col" style="left:588px">
    <h4>Follow Us</h4>
    <ul>
      <li><span class="sq"></span>Pinloop</li>
      <li><span class="sq"></span>Chirpwell</li>
      <li><span class="sq"></span>Snapfold</li>
      <li><span class="sq"></span>Reelcast</li>
      <li><span class="sq"></span>Workmesh</li>
    </ul>
  </div>

  <div class="footer-col" style="left:774px"><h4>Get in Touch</h4></div>
  <form class="form">
    <div class="field" style="left:0;top:0;width:179px;height:30px">Name</div>
    <div class="field" style="left:184px;top:0;width:182px;height:30px">Email</div>
    <div class="field" style="left:0;top:37px;width:366px;height:30px">Address</div>
    <div class="field" style="left:0;top:75px;width:366px;height:57px">Message</div>
    <a class="btn submit">Submit</a>
  </form>
</footer>

<div class="copyright">Copyright © 2018 - www.lumovale.test . All Rights Reserved.</div>

</body>
</html>
```